TEK Logistics - Banner 2.5' x 8' for 20+ locations

Need a banner designed that will pop. This banner will be displayed at over 20 of our transportation facilities. Goal is for the banner to grab the attention of employees, contractors and clients and help reinforce our mission and core values. Designed needs to include TEK Logo, our core values and mission statement. Red and Black are the main company colors and we need to stay within that theme and color pallet. Attached is a previous version that was too basic and boring. Willing to consider a design that excludes the mission statement.

Gathering more feedback

```html
<!DOCTYPE html>
<html lang="en">
<head>
<meta charset="utf-8">
<title>TEK Logistics – Core Values Banner</title>
<link href="https://fonts.googleapis.com/css2?family=Exo+2:wght@600;700&family=Montserrat:wght@700&display=swap" rel="stylesheet">
<style>
  :root {
    --brand-red: #d12727;
    --brand-black: #2b2a29;
    --paper: #ffffff;
    --backdrop: #d6d6d6;
  }
  * { margin: 0; padding: 0; box-sizing: border-box; }
  html, body {
    width: 1200px; height: 970px; overflow: hidden;
    background: var(--backdrop);
  }
  .canvas { position: relative; width: 1200px; height: 970px; }
  .banner {
    position: absolute; left: 28.6px; top: 306.5px;
    width: 1843px; height: 576px;
    transform: scale(0.62); transform-origin: top left;
    overflow: hidden; background: var(--paper);
  }
  .banner-shapes { position: absolute; inset: 0; }

  .values-title {
    position: absolute; left: 85px; top: 52px;
    font: 700 56px/1 "Exo 2", sans-serif;
    color: var(--brand-black); letter-spacing: 1px;
  }
  .values-title .accent { color: var(--brand-red); }
  .values-rule {
    position: absolute; left: 86px; top: 118px;
    width: 101px; height: 4px; background: var(--brand-black);
  }
  .values-list { position: absolute; left: 86px; top: 160px; list-style: none; }
  .value-item {
    display: flex; align-items: center; height: 62.4px;
    font: 700 25.5px/1 Montserrat, sans-serif; color: var(--brand-black);
  }
  .value-icon { width: 56px; height: 56px; margin-right: 10px; flex: none; }

  .mission {
    position: absolute; left: 742px; width: 500px; top: 146px;
    text-align: center;
  }
  .mission-title {
    font: 700 58px/1 "Exo 2", sans-serif; color: var(--brand-black);
  }
  .mission-subtitle {
    font: 600 31px/1 "Exo 2", sans-serif; color: var(--brand-black);
    letter-spacing: 6px; margin-top: 2px;
  }
  .mission-rule {
    width: 100px; height: 3px; background: var(--brand-black);
    margin: 7px auto 0;
  }
  .mission-text {
    margin-top: 18px;
    font: 700 31.5px/38.5px Montserrat, sans-serif; color: var(--paper);
  }

  .brand-name {
    position: absolute; left: 1495px; top: 118px; width: 250px;
    text-align: center; color: var(--paper);
    font: 700 92px/1 "Exo 2", sans-serif;
  }
  .brand-name .brand-sub {
    display: block; font-size: 32px; letter-spacing: 7px; margin-top: 2px;
    padding-left: 7px;
  }
</style>
</head>
<body>
<div class="canvas">
  <section class="banner" aria-label="TEK Logistics core values and mission banner">
    <svg class="banner-shapes" viewBox="0 0 1843 576" aria-hidden="true">
      <rect width="1843" height="576" fill="var(--brand-red)"/>
      <rect width="992" height="576" fill="var(--paper)"/>
      <circle cx="992" cy="355" r="360" fill="var(--paper)"/>
      <path d="M732,205 A305,305 0 0 1 1292,345 A330,300 0 0 0 732,205 Z" fill="var(--brand-black)"/>
      <circle cx="992" cy="353" r="285" fill="var(--brand-red)"/>
      <path d="M1343,152 C1440,250 1480,420 1395,576 L1315,576 C1395,430 1410,280 1343,152 Z" fill="var(--brand-black)"/>
      <path d="M1420,207 C1510,290 1560,440 1515,576 L1440,576 C1500,440 1490,300 1420,207 Z" fill="var(--brand-black)"/>
    </svg>

    <h2 class="values-title"><span class="accent">CORE</span> VALUES</h2>
    <div class="values-rule"></div>
    <ul class="values-list">
      <li class="value-item">
        <svg class="value-icon" viewBox="0 0 56 56"><circle cx="30" cy="30" r="25" fill="var(--brand-red)"/><circle cx="26" cy="26" r="25" fill="var(--paper)"/><circle cx="26" cy="26" r="23" fill="var(--brand-black)"/><path d="M16 36V24h5v12zM23 36V24l6-9c2 0 3 1 3 3l-1 5h6c2 0 3 2 2 4l-3 7c-1 1-2 2-3 2z" fill="var(--paper)"/></svg>
        Do the right things for the right reasons</li>
      <li class="value-item">
        <svg class="value-icon" viewBox="0 0 56 56"><circle cx="30" cy="30" r="25" fill="var(--brand-red)"/><circle cx="26" cy="26" r="25" fill="var(--paper)"/><circle cx="26" cy="26" r="23" fill="var(--brand-black)"/><path d="M26 12v18M26 20c-5 0-7-3-7-5 4 0 7 2 7 5zM26 24c5 0 7-3 7-5-4 0-7 2-7 5z" stroke="var(--paper)" stroke-width="2.5" fill="var(--paper)"/><path d="M19 31h14l-2 9H21z" fill="var(--paper)"/></svg>
        Pursue growth and development</li>
      <li class="value-item">
        <svg class="value-icon" viewBox="0 0 56 56"><circle cx="30" cy="30" r="25" fill="var(--brand-red)"/><circle cx="26" cy="26" r="25" fill="var(--paper)"/><circle cx="26" cy="26" r="23" fill="var(--brand-black)"/><g fill="var(--paper)"><circle cx="17" cy="18" r="3"/><circle cx="26" cy="16" r="3.5"/><circle cx="35" cy="18" r="3"/><rect x="14" y="23" width="6" height="13" rx="2"/><rect x="22.5" y="22" width="7" height="16" rx="2"/><rect x="32" y="23" width="6" height="13" rx="2"/></g></svg>
        Build a positive team atmosphere</li>
      <li class="value-item">
        <svg class="value-icon" viewBox="0 0 56 56"><circle cx="30" cy="30" r="25" fill="var(--brand-red)"/><circle cx="26" cy="26" r="25" fill="var(--paper)"/><circle cx="26" cy="26" r="23" fill="var(--brand-black)"/><path d="M13 27l25-10-8 22-5-8z" fill="var(--paper)"/></svg>
        Deliver WOW through service</li>
      <li class="value-item">
        <svg class="value-icon" viewBox="0 0 56 56"><circle cx="30" cy="30" r="25" fill="var(--brand-red)"/><circle cx="26" cy="26" r="25" fill="var(--paper)"/><circle cx="26" cy="26" r="23" fill="var(--brand-black)"/><path d="M28 11l8 3v6c0 5-4 8-8 9-4-1-8-4-8-9v-6z" fill="var(--paper)"/><path d="M24 20l3 3 5-5" stroke="var(--brand-black)" stroke-width="2" fill="none"/><path d="M12 34h8l6 3h8l-4 4H20l-8-2z" fill="var(--paper)"/></svg>
        Do everything Safely</li>
      <li class="value-item">
        <svg class="value-icon" viewBox="0 0 56 56"><circle cx="30" cy="30" r="25" fill="var(--brand-red)"/><circle cx="26" cy="26" r="25" fill="var(--paper)"/><circle cx="26" cy="26" r="23" fill="var(--brand-black)"/><g fill="var(--paper)"><circle cx="26" cy="24" r="4"/><path d="M19 37l2-8h10l2 8z"/><circle cx="15" cy="20" r="2"/><circle cx="19" cy="13" r="2"/><circle cx="26" cy="11" r="2"/><circle cx="33" cy="13" r="2"/><circle cx="37" cy="20" r="2"/></g></svg>
        Have Fun</li>
    </ul>

    <div class="mission">
      <h2 class="mission-title">MISSION</h2>
      <p class="mission-subtitle">STATEMENT</p>
      <div class="mission-rule"></div>
      <p class="mission-text">Provide the best<br>customer experience while<br>creating an environment of<br>growth and opportunity for<br>our customers, employees,<br>and service providers.</p>
    </div>

    <p class="brand-name">TEK<span class="brand-sub">LOGISTICS</span></p>
  </section>
</div>
</body>
</html>
```